female stress management consultant, doctor, Health & Well-being coach needs a wordpress theme

I am a Stress management consultant, General Practitioner and Health and Well-Being coach who is targeting mainly surgeries/hospitals and corporate business.
I have my own URL drhelgabrunsvik.com and the hosting.
I need a WordPress Website that is easy to maintain and edit to regularly change the content (copy/pictures/action buttons/banners).
I want my website to look professional and elegant for corporate businesses and managers to feel they can trust me and my expertise. At the same time, the website should have a warm and welcoming feel to it. It should feel uplifting and very positive.
I am open to colour suggestions, but please incorporate the following two colours: #F18877 and #D2BB7A. For fonts I prefer grey over black (like #777777).
The website needs to create an impression of "know like and trust".
The website should have a sign-up button for a newsletter, multiple contact buttons over the home page - to write an email to me, contact details top and bottom and the possibility to have a video on the home page top instead of a picture (Best would be that I can change from picture to video to picture in the future without needing a designer). A video that can run in the background with text laid over. A bit like on this website from Tessa Vanrijn: https://www.tessavanrijn.com.
I need 5 pages: Home, About, Services, Contact, free resources. I do NOT need an e-commerce or booking facility as I will neither sell nor let people book through my website. I don't need a blog either.
All the pages need to have a link to my other website (brightpathdaily.co.uk) and it needs to state that the linked website (brightpathdaily) is my website with a blog and for private customers.
Please use the photos I attached if possible. Me with the dogs for the "about" section.

Websites I like: https://www.olgabkr.com, tessavanrijn.com, https://ruthpembly.com (this site is too dark for my liking, but the layout has a simple navigation layout, the important buttons are right up at the side (WorkLattice/social media/CTA), is minimalistic - hence easy to find the important bits).

Target Market(s)

surgeries/doctor offices, hospitals, corporate business

Industry/Entity Type

Health and well-being

Coding

Coded - Design and coding required

Number of Pages Required

5+ page

Font styles to use
Sans Serif

Requirements
Must have
• see project description
Nice to have
• see project description

```html
<!DOCTYPE html>
<html lang="en">
<head>
<meta charset="utf-8">
<title>Dr Helga Brunsvik — Stress Management &amp; Well-being</title>
<link rel="stylesheet" href="https://fonts.googleapis.com/css2?family=Oswald:wght@400;500&family=Montserrat:wght@400;500;600;700&family=Poppins:wght@500&display=swap">
<style>
:root{
  --salmon:#F18877;
  --salmon-dark:#E57B69;
  --gold:#D2BB7A;
  --grey:#777777;
  --dark:#3c3c3c;
  --white:#ffffff;
  --heading:"Oswald",sans-serif;
  --body:"Montserrat",sans-serif;
}
*{box-sizing:border-box;margin:0;padding:0}
html,body{width:1200px;height:4857px;overflow:hidden;background:#fff}
body{font-family:var(--body);color:var(--grey);position:relative}
.abs{position:absolute}
b{font-weight:700;color:#555}
.btn{position:absolute;display:flex;align-items:center;justify-content:center;border-radius:20px;font:700 10px/1 var(--body);letter-spacing:.4px;text-transform:uppercase;color:#fff;background:var(--salmon);box-shadow:0 3px 8px rgba(241,136,119,.35)}
.btn-ghost{background:transparent;border:1.5px solid #fff;box-shadow:none;font-weight:500}
.btn-ghost-gold{background:#fff;border:1.5px solid var(--gold);color:var(--gold);box-shadow:none;font-weight:500}
.divider{position:absolute;height:2px;background:var(--grey);width:44px}
.divider::after{content:"";position:absolute;left:50px;top:0;width:20px;border-top:2px dotted var(--grey)}

/* top bar */
.topbar{left:0;top:0;width:1200px;height:32px;background:var(--salmon);color:#fff;font-size:10px}
.topbar .contact{position:absolute;top:9px;display:flex;align-items:center;gap:6px}
.socials{position:absolute;top:10px;left:843px;display:flex;gap:14px}
.socials span{width:11px;height:11px;border-radius:50%;background:#fff;display:block}

/* header */
.header{left:0;top:32px;width:1200px;height:87px;background:#fff}
.logo{position:absolute;display:flex;align-items:center;gap:6px}
.logo-dot{width:26px;height:26px;border-radius:50%;background:var(--salmon)}
.logo-name{font:500 13px var(--body);color:var(--salmon)}
.nav{position:absolute;left:391px;top:36px;display:flex;gap:20px;font-size:11.5px;color:var(--grey)}
.nav .active{color:var(--salmon)}
.header .cta{left:957px;top:28px;width:153px;height:31px;border-radius:2px;font-weight:500;box-shadow:none}

/* hero */
.hero{left:0;top:119px;width:1200px;height:477px;background:linear-gradient(120deg,#4a4a4a,#6b6660 45%,#3e3c3a);}
.hero::after{content:"";position:absolute;inset:0;background:rgba(30,30,30,.35)}
.hero-content{position:absolute;left:226px;top:132px;z-index:1;color:#fff;width:480px}
.eyebrow{display:flex;align-items:center;gap:10px;font:600 10px var(--body)}
.eyebrow::before{content:"";width:30px;height:2px;background:var(--salmon)}
.hero h1{font:500 38px/46px var(--heading);margin-top:14px}
.hero h1 .hearts{color:#e0262c}
.hero p{font:600 11px/16px var(--body);margin-top:10px}

/* about */
.about-hi{left:226px;top:702px;display:flex;align-items:center;gap:14px;font:500 18px var(--body);color:var(--gold)}
.about-hi::before{content:"";width:30px;height:2px;background:var(--gold)}
.about-name{left:234px;top:738px;font:500 33px var(--heading);color:var(--salmon)}
.about-role{left:234px;top:792px;width:380px;font:500 13.5px/19px var(--body);color:#333}
.about-text{left:234px;top:838px;width:380px;font:400 11px/26px var(--body)}
.about-text-me{left:234px;top:922px;font:500 14px var(--body);color:#333;display:flex;align-items:center;gap:6px}
.about-text-me::before{content:"";width:12px;height:12px;background:var(--gold);border-radius:50%}
.photo{background:linear-gradient(160deg,#6e8a4b,#9aa874 50%,#55693a)}

/* banners */
.band{left:8px;width:1192px}
.panel{position:absolute;background:rgba(210,187,122,.82);padding:38px 20px}
.panel h2{font:400 20px/38px var(--heading);color:var(--salmon);text-transform:none}
.panel p{font:500 11px/17px var(--body);color:#8d7d55}

/* section heads */
.section-title{position:absolute;left:0;width:1200px;text-align:center;font:500 31px var(--heading);color:var(--salmon)}
.section-lead{position:absolute;text-align:center;font:500 11.2px/17px var(--body);color:var(--grey)}

/* services */
.service{position:absolute;top:1874px;width:244px}
.service .img{height:147px}
.service h3{font:400 20px/38px var(--heading);color:var(--salmon);margin:10px 0 0 13px;text-transform:uppercase}
.service h4{font:500 17px/30px var(--heading);color:#555;text-transform:uppercase;margin-left:13px}
.service p{font:500 10.6px/17px var(--body);margin-left:13px;width:215px}
.service .divider{position:relative;margin:14px 0 18px 13px;display:block;width:44px}

/* testimonials */
.t-card{position:absolute;top:3264px;width:225px;height:416px;background:#fff;box-shadow:0 6px 16px rgba(0,0,0,.10);text-align:center;padding:26px 14px}
.t-quote{font:400 54px/40px var(--heading);color:var(--salmon)}
.t-card h3{font:500 17px/22px var(--body);color:#333;margin-top:16px}
.t-card p{font:400 9px/15px var(--body);margin-top:12px}
.t-person{position:absolute;top:3650px;width:225px;text-align:center}
.avatar{width:48px;height:48px;border-radius:50%;background:linear-gradient(#c59774,#8b5e3f);margin:0 auto}
.t-person .name{font:700 10.5px var(--body);color:#333;margin-top:20px}
.t-person .role{font:400 8px var(--body);color:#999;margin-top:4px}

/* closing */
.closing-panel{left:600px;top:3897px;width:378px;height:560px;background:var(--gold);padding:46px 20px}
.closing-panel h2{font:400 20px/38px var(--heading);color:var(--salmon)}
.closing-panel h4{font:500 17px var(--heading);color:#555;margin-top:52px}
.closing-panel p{font:500 10.6px/17px var(--body);color:#77693f;margin-top:14px}
.closing-panel p b{color:#6a5b30}

/* footer */
.footer-title{font:400 17px var(--heading);color:var(--salmon)}
.footer-link{font:400 9.5px var(--body);color:#888}
.subscribe{left:755px;top:4648px;width:215px;height:32px;border:1.5px solid var(--salmon);border-radius:16px;font-size:9px;padding:10px 14px;color:#666}
.subscribe-btn{left:940px;top:4650px;width:28px;height:28px;border-radius:50%;background:var(--salmon)}
.foot-social{left:236px;top:4728px;display:flex;gap:16px}
.foot-social span{width:18px;height:18px;border-radius:50%;border:1px solid #ccc;display:block}
.bottombar{left:0;top:4803px;width:1200px;height:54px;background:var(--salmon);color:#fff;font:500 9px var(--body)}
</style>
</head>
<body>

<!-- top bar -->
<div class="abs topbar">
  <div class="contact" style="left:230px">
    <svg width="12" height="12" viewBox="0 0 24 24" fill="none" stroke="#fff" stroke-width="2"><path d="M5 3h4l2 5-3 2a11 11 0 0 0 6 6l2-3 5 2v4a2 2 0 0 1-2 2A17 17 0 0 1 3 5a2 2 0 0 1 2-2z"/></svg>
    +1 (555)-014-2233
  </div>
  <div class="contact" style="left:372px">
    <svg width="13" height="12" viewBox="0 0 24 20" fill="none" stroke="#fff" stroke-width="2"><rect x="2" y="2" width="20" height="16"/><path d="M2 3l10 8 10-8"/></svg>
    info@drhelgabrunsvik.com
  </div>
  <div class="socials"><span></span><span></span><span></span><span></span><span></span></div>
</div>

<!-- header -->
<header class="abs header">
  <div class="logo" style="left:28px;top:28px"><span class="logo-dot"></span><span class="logo-name">Dr Helga Brunsvik</span></div>
  <nav class="nav"><span class="active">Home</span><span>About</span><span>Services</span><span>Contact</span><span>Free Resources</span></nav>
  <div class="btn cta">BRIGHTPATHDAILY</div>
</header>

<!-- hero -->
<section class="abs hero" role="img" aria-label="Background photo of a woman and child on a staircase">
  <div class="hero-content">
    <div class="eyebrow">LIVE YOUR BEST LIFE: HAPPY &amp; HEALTHY &amp; FULL OF JOY!</div>
    <h1>Manage your Stress and Live<br>the Life you Love <span class="hearts">♥♥♥</span></h1>
    <p>Lorem ips um dolor sit amet, consectetur adipiscing elit. Lorem ipsum dolor sit amet, consectetur adipiscing elit. Lorem ipsum dolor sit amet, consectetur adipiscing elit.</p>
  </div>
</section>
<div class="btn" style="left:228px;top:455px;width:127px;height:37px">About me</div>
<div class="btn btn-ghost" style="left:379px;top:455px;width:157px;height:37px">Contact me</div>

<!-- about -->
<div class="abs about-hi">Hi, I am</div>
<h2 class="abs about-name">DR HELGA BRUNSVIK, MD, PHD</h2>
<p class="abs about-role">Medical doctor and General Practitioner, certified Health and Well-being Coach...</p>
<p class="abs about-text">Lorem ipm um dolor sit amet, consectetur adipiscing elit. Lorem ipsum dolor sit amet, consectetur adipiscing elit. Lorem ipsum dolor sit amet, consectetur adipiscing elit.</p>
<div class="abs about-text-me">Text me! 555-010-4417</div>
<div class="btn" style="left:228px;top:958px;width:127px;height:38px">About me</div>
<div class="btn btn-ghost-gold" style="left:362px;top:958px;width:157px;height:38px">Contact me</div>
<div class="abs photo" style="left:645px;top:688px;width:327px;height:305px" role="img" aria-label="Photo of the doctor kneeling on grass with her two dogs"></div>

<!-- sea banner -->
<section class="abs band" style="top:1098px;height:438px;background:linear-gradient(180deg,#2f6a93 0%,#4f8fb4 40%,#d9e6ea 62%,#6c97a8 78%,#8fa7a9 100%)" role="img" aria-label="Photo of ocean waves breaking on a beach">
  <div class="panel" style="left:218px;top:29px;width:380px;height:383px">
    <h2>Revitalise Your Life with Ease: Master the Art of Self-Care in Simple, yet Powerful Ways!</h2>
    <div class="divider" style="left:20px;top:192px;background:#8d7d55"></div>
    <p style="margin-top:46px">You have the <b>power</b> to <b>shape the life you truly love</b> every single day! Believe it or not, <b>your influence over your health and well-being is even greater than you realise</b>. It's <b>easier</b> than you think! Let's create a life that brings you joy. <b>I'm here for you!</b></p>
  </div>
</section>
<div class="btn" style="left:247px;top:1449px;width:136px;height:38px">Start here</div>

<!-- how I help -->
<h2 class="section-title" style="top:1648px">HOW I HELP</h2>
<div class="divider" style="left:556px;top:1706px"></div>
<p class="section-lead" style="left:234px;top:1742px;width:732px">You have the <b>power</b> to <b>shape the life you truly love</b> every single day! Believe it or not, <b>your influence over your health and well-being is even greater than you realise</b>. It's <b>easier</b> than you think! Let's create a life that brings you joy. <b>I'm here for you!</b></p>

<div class="service" style="left:221px">
  <div class="img" style="background:linear-gradient(180deg,#b9c7a4,#6f8f45 60%,#4f6e2f)" role="img" aria-label="Photo of the doctor laughing with open arms in a meadow"></div>
  <h3>1:1 Coaching online or in person</h3>
  <span class="divider"></span>
  <h4>Get personal support</h4>
  <p style="margin-top:14px">You have the <b>power</b> to <b>shape the life you truly love</b> every single day! Believe it or not, <b>your influence over your health and well-being is even greater than you realise</b>. It's <b>easier</b> than you think! Let's create a life that brings you joy. <b>I'm here for you!</b></p>
</div>
<div class="service" style="left:477px">
  <div class="img" style="background:linear-gradient(160deg,#5a6b52,#8d9a80 50%,#3f4a39)" role="img" aria-label="Photo of a woman blowing soap bubbles"></div>
  <h3>Talks &amp; Workshops for<br>Health &amp; Wellbeing</h3>
  <span class="divider"></span>
  <h4>Get motivated and into action</h4>
  <p style="margin-top:14px">You have the <b>power</b> to <b>shape the life you truly love</b> every single day! Believe it or not, <b>your influence over your health and well-being is even greater than you realise</b>. It's <b>easier</b> than you think! Let's create a life that brings you joy. <b>I'm here for you!</b></p>
</div>
<div class="service" style="left:734px">
  <div class="img" style="background:linear-gradient(160deg,#6e8a4b,#a2ad7e 50%,#55693a)" role="img" aria-label="Photo of the doctor with her dogs on grass"></div>
  <h3>Intentional Creativity.</h3>
  <span class="divider" style="margin-top:24px"></span>
  <h4>Unlocking your inner world</h4>
  <p style="margin-top:14px">You have the <b>power</b> to <b>shape the life you truly love</b> every single day! Believe it or not, <b>your influence over your health and well-being is even greater than you realise</b>. It's <b>easier</b> than you think! Let's create a life that brings you joy. <b>I'm here for you!</b></p>
</div>
<div class="btn" style="left:234px;top:2425px;width:187px;height:37px">More information</div>
<div class="btn" style="left:491px;top:2425px;width:187px;height:37px">More information</div>
<div class="btn" style="left:748px;top:2425px;width:187px;height:37px">More information</div>

<!-- sunset banner -->
<section class="abs band" style="top:2538px;height:398px;background:linear-gradient(160deg,#e6c98a 0%,#f6e3b0 35%,#fbf0d2 55%,#e9c486 100%)" role="img" aria-label="Photo of hands releasing a butterfly against a sunset">
  <div class="panel" style="left:218px;top:28px;width:380px;height:370px">
    <h2>LIVE YOUR BEST LIFE: !<br>HAPPY &amp; HEALTHY &amp; FULL OF JOY</h2>
    <p style="margin-top:36px">You have the <b>power</b> to <b>shape the life you truly love</b> every single day! Believe it or not, <b>your influence over your health and well-being is even greater than you realise</b>. It's <b>easier</b> than you think! Let's create a life that brings you joy. <b>I'm here for you!</b></p>
  </div>
</section>
<div class="btn" style="left:247px;top:2851px;width:246px;height:36px">Start your exciting future</div>

<!-- testimonials -->
<h2 class="section-title" style="top:3082px;text-transform:none">Testimonial</h2>
<div class="divider" style="left:556px;top:3136px"></div>
<p class="section-lead" style="left:247px;top:3172px;width:706px">You have the <b>power</b> to <b>shape the life you truly love</b> every single day! Believe it or not, <b>your influence over your health and well-being is even greater than you realise</b>. It's <b>easier</b> than you think! Let's create a life that brings you joy. <b>I'm here for you!</b></p>

<div class="t-card" style="left:243px"><div class="t-quote">99</div><h3>I've learned that I am enough and that I can be my authentic self</h3><p>It has been an incredible experience, and I loved every minute of it! I have gained so much from this course; the biggest one that stands out to me is knowing I am enough and can be my authentic self. I would have no hesitation whatsoever ever to recommend Dr Helga to anyone. I feel many would benefit from working with Dr Helga, as I know their lives would become more enriched!</p></div>
<div class="t-card" style="left:487px"><div class="t-quote">99</div><h3>I've learned that I am enough and that I can be my authentic self</h3><p>It has been an incredible experience, and I loved every minute of it! I have gained so much from this course; the biggest one that stands out to me is knowing I am enough and can be my authentic self. I would have no hesitation whatsoever ever to recommend Dr Helga to anyone. I feel many would benefit from working with Dr Helga, as I know their lives would become more enriched!</p></div>
<div class="t-card" style="left:730px"><div class="t-quote">99</div><h3>I've learned that I am enough and that I can be my authentic self</h3><p>It has been an incredible experience, and I loved every minute of it! I have gained so much from this course; the biggest one that stands out to me is knowing I am enough and can be my authentic self. I would have no hesitation whatsoever ever to recommend Dr Helga to anyone. I feel many would benefit from working with Dr Helga, as I know their lives would become more enriched!</p></div>

<div class="t-person" style="left:243px"><div class="avatar" role="img" aria-label="Portrait of the client"></div><div class="name">Anna Lindqvist</div><div class="role">Yoga Therapist</div></div>
<div class="t-person" style="left:487px"><div class="avatar" role="img" aria-label="Portrait of the client"></div><div class="name">Anna Lindqvist</div><div class="role">Yoga Therapist</div></div>
<div class="t-person" style="left:730px"><div class="avatar" role="img" aria-label="Portrait of the client"></div><div class="name">Anna Lindqvist</div><div class="role">Yoga Therapist</div></div>
<div class="abs" style="left:588px;top:3787px;width:11px;height:11px;border-radius:50%;background:var(--salmon)"></div>
<div class="abs" style="left:604px;top:3790px;width:6px;height:6px;border-radius:50%;background:#ddd"></div>

<!-- closing -->
<section class="abs" style="left:0;top:3844px;width:1200px;height:666px;background:linear-gradient(160deg,#9fb48a 0%,#d9dfcf 30%,#7e9b55 65%,#57782f 100%)" role="img" aria-label="Photo of the doctor laughing with arms spread in a flowering meadow"></section>
<div class="abs closing-panel">
  <h2>UNLOCK THE POWER OF JOY AND WELL-BEING: DISCOVER SIMPLE STEPS TO RESTORE YOUR HAPPINESS AND HEALTH TODAY!</h2>
  <div class="divider" style="left:20px;top:202px;background:#555"></div>
  <h4>UNLOCKING YOUR INNER WORLD</h4>
  <p>With over <b>30 years of being a doctor</b>, I've met countless people facing ongoing health issues and struggles that couldn't be solved solely through conventional medicine. That's why <b>it's so important to embrace a holistic approach</b> in our quest for balance, shifting from discomfort to vitality and contentment.</p>
  <p style="margin-top:8px"><b>The secret to living a joyful, vibrant life lies in nurturing every aspect of yourself</b>, not just your physical body. Surprisingly, it's easier as you might think to harmonize your body, mind, and spirit and experience optimal well-being.</p>
</div>
<div class="btn" style="left:619px;top:4399px;width:187px;height:36px">More information</div>

<!-- footer -->
<div class="logo" style="left:226px;top:4610px;position:absolute"><span class="logo-dot"></span><span class="logo-name">Dr Helga Brunsvik</span></div>
<div class="abs footer-link" style="left:262px;top:4640px;font-size:7px">Create a life you love living</div>
<div class="abs footer-title" style="left:492px;top:4572px">Useful Links</div>
<div class="abs footer-link" style="left:498px;top:4612px">About Me</div>
<div class="abs footer-link" style="left:498px;top:4640px">Services</div>
<div class="abs footer-link" style="left:623px;top:4612px">Contact Us</div>
<div class="abs footer-link" style="left:623px;top:4640px">Free Resources</div>
<div class="abs footer-title" style="left:755px;top:4572px">Subscribe Now</div>
<div class="abs footer-link" style="left:755px;top:4606px;width:230px;font-size:8.5px;line-height:14px">GET REGULAR INSPIRATION FOR HEALTH, WELLBEING AND HAPPINESS</div>
<div class="abs subscribe">Your mail here</div>
<div class="abs subscribe-btn"></div>
<div class="abs foot-social"><span></span><span></span><span></span><span></span><span></span></div>

<div class="abs bottombar">
  <span class="abs" style="left:226px;top:22px">©2023. Dr Helga Brunsvik. All Rights Reserved.</span>
  <span class="abs" style="left:774px;top:22px">Home</span>
  <span class="abs" style="left:815px;top:22px">Contact Us</span>
  <span class="abs" style="left:880px;top:22px">Bright Path Daily</span>
</div>

</body>
</html>
```